Nail Salon Business Card Design Project

We would like a business card design for a new nail salon using a logo supplied in eps format.

Depending on the success of this we will be creating projects for a price list, gift voucher and website design later also.

The business is called "Velvet Nail Salon". We provide manicure, spa pedicure and waxing services to professional ladies in the 30's age group.

The salon is very modern, clean, open and bright.

Target Market(s)

Ladies in their 30s.

Industry/Entity Type

Salon

Requirements
Must have
• On the front of the card we would like:
- the logo (see attached)
- address (Shop 14 Tallowood Grove Shopping Centre
Kestrel Avenue
Canberra Airport ACT 2617)
- website address (www.velvetnails.example.com.au)
- email (jm@velvetnails.example.com.au)
- phone number (0412-758-031)

On the back we would like the trading hours, a grid/table (5 columns by 3 rows) for loyalty stamps, and an area for writing the customers next appointment. See attached for sample of content (card back.jpg).
Nice to have
• If possible it would be nice to have:
- a photo image
- facebook site address (http://www.facebook.com/velvetnailsalonaustralia)

I'm willing to pay extra (around $100) for the image if it can also be used on stationary and the website (projects for later).

```html
<!DOCTYPE html>
<html lang="en">
<head>
<meta charset="utf-8">
<title>Velvet Nail Salon – Business Card</title>
<link href="https://fonts.googleapis.com/css2?family=Source+Sans+3:wght@400;600&display=swap" rel="stylesheet">
<style>
  :root {
    --bg: #ecebe8;
    --card: #ffffff;
    --panel-top: #ebebeb;
    --panel-bottom: #dcdcdc;
    --pink: #e0649e;
    --grey-logo: #a9a9a9;
    --text: #3d3d3d;
    --text-dark: #111111;
    --rule: #a6a6a6;
    --ornament: #f3f3f3;
  }
  * { margin: 0; padding: 0; box-sizing: border-box; }
  html, body { width: 1200px; height: 559px; overflow: hidden; }
  body {
    background: var(--bg);
    font-family: "Source Sans 3", "Myriad Pro", Arial, sans-serif;
    color: var(--text);
    position: relative;
  }
  .card {
    position: absolute;
    top: 136px;
    height: 286px;
    background: var(--card);
    overflow: hidden;
    box-shadow: 0 2px 6px rgba(0,0,0,0.18);
  }
  .card--front { left: 47px; width: 507px; }
  .card--back  { left: 583px; width: 510px; }

  /* Front */
  .front-ornament {
    position: absolute; left: 0; top: 150px; width: 230px; height: 136px;
    background: radial-gradient(ellipse at 45% 40%, var(--ornament), rgba(255,255,255,0) 70%);
  }
  .wordmark {
    position: absolute; text-align: right; font-weight: 400; line-height: 1;
  }
  .wordmark__name { display: block; font-size: 40px; letter-spacing: 7px; }
  .wordmark__sub  { display: block; font-size: 13px; letter-spacing: 1.5px; margin-top: 4px; margin-right: 6px; }
  .card--front .wordmark { left: 30px; top: 122px; width: 252px; color: var(--pink); }

  .contact-panel {
    position: absolute; left: 300px; top: 0; width: 207px; height: 100%;
    background: linear-gradient(180deg, var(--panel-top), var(--panel-bottom));
  }
  .portrait {
    position: absolute; left: 55px; top: 10px; width: 68px; height: 102px;
    border-radius: 0 0 10px 0;
    background: linear-gradient(180deg, #6b5344 0%, #b88a6e 45%, #3a3a3a 100%);
  }
  .person-name {
    position: absolute; left: 30px; top: 124px; font-size: 17px; color: var(--text-dark);
  }
  .address {
    position: absolute; left: 30px; top: 167px; font-size: 12px; line-height: 15px;
  }
  .contact-list {
    position: absolute; left: 16px; top: 206px; right: 6px;
    list-style: none; font-size: 11px; white-space: nowrap;
  }
  .contact-list li { display: flex; align-items: center; height: 19px; }
  .contact-list svg { width: 11px; height: 11px; margin-right: 7px; flex: none; }

  /* Back */
  .info-panel {
    position: absolute; left: 0; top: 0; width: 225px; height: 100%;
    background: linear-gradient(180deg, var(--panel-top), var(--panel-bottom));
  }
  .info-block { position: absolute; left: 54px; font-size: 12px; line-height: 15px; }
  .info-heading { color: var(--pink); font-size: 12.5px; font-weight: 400; margin-bottom: 3px; }
  .hours p + p { margin-top: 5px; }
  .hours { top: 25px; }
  .loyalty { top: 125px; }
  .stamp-grid { border-collapse: collapse; margin-top: 2px; }
  .stamp-grid td {
    width: 25px; height: 18px; border: 1px solid var(--rule); background: #fff;
  }
  .appointment { top: 217px; line-height: 14.5px; }

  .card--back .wordmark { left: 290px; top: 74px; width: 200px; color: var(--grey-logo); }
  .card--back .wordmark__name { font-size: 32px; letter-spacing: 6px; }
  .card--back .wordmark__sub  { font-size: 11px; }
  .nail-art {
    position: absolute; left: 370px; top: 150px; width: 140px; height: 136px;
    background: linear-gradient(135deg, rgba(255,255,255,0) 10%, #efe3d6 35%, #e2a794 70%, #d88f80 100%);
    clip-path: polygon(45% 0, 100% 20%, 100% 100%, 10% 100%, 0 60%);
  }
</style>
</head>
<body>

<section class="card card--front">
  <div class="front-ornament" role="img" aria-label="Faint grey floral flourish"></div>
  <div class="wordmark">
    <span class="wordmark__name">Velvet</span>
    <span class="wordmark__sub">Nail Salon</span>
  </div>

  <div class="contact-panel">
    <div class="portrait" role="img" aria-label="Portrait photo of the staff member"></div>
    <p class="person-name">Name here</p>
    <p class="address">Complex Name, Street Area,<br>City Name,000 000</p>
    <ul class="contact-list">
      <li>
        <svg viewBox="0 0 12 12" aria-hidden="true"><rect x="3" y="0.5" width="6" height="11" rx="1.2" fill="var(--pink)"/><rect x="4.2" y="2" width="3.6" height="5" fill="#fff"/></svg>
        1234567890
      </li>
      <li>
        <svg viewBox="0 0 12 12" aria-hidden="true"><circle cx="6" cy="6" r="2" fill="none" stroke="var(--pink)" stroke-width="1.4"/><path d="M8 4v2.8c0 1 1.8 1 1.8-.8A3.8 3.8 0 1 0 7.5 9.6" fill="none" stroke="var(--pink)" stroke-width="1.4"/></svg>
        jm@velvetnails.example.com.au
      </li>
      <li>
        <svg viewBox="0 0 12 12" aria-hidden="true"><circle cx="6" cy="6" r="5" fill="none" stroke="var(--pink)" stroke-width="1.2"/><ellipse cx="6" cy="6" rx="2.2" ry="5" fill="none" stroke="var(--pink)" stroke-width="1"/><path d="M1 6h10" stroke="var(--pink)" stroke-width="1"/></svg>
        www.velvetnails.example.com.au
      </li>
    </ul>
  </div>
</section>

<section class="card card--back">
  <div class="info-panel">
    <div class="info-block hours">
      <h3 class="info-heading">Trading Hours</h3>
      <p>Monday to Friday<br>9.30am to 5.30pm</p>
      <p>Saturday<br>9.30am to 1pm</p>
    </div>
    <div class="info-block loyalty">
      <h3 class="info-heading">loyalty stamps</h3>
      <table class="stamp-grid" aria-label="Loyalty stamp grid">
        <tr><td></td><td></td><td></td><td></td><td></td></tr>
        <tr><td></td><td></td><td></td><td></td><td></td></tr>
        <tr><td></td><td></td><td></td><td></td><td></td></tr>
      </table>
    </div>
    <div class="info-block appointment">
      <h3 class="info-heading">Appointment</h3>
      <p>Date...............</p>
      <p>Day................</p>
      <p>Time...............</p>
    </div>
  </div>

  <div class="wordmark">
    <span class="wordmark__name">Velvet</span>
    <span class="wordmark__sub">Nail Salon</span>
  </div>
  <div class="nail-art" role="img" aria-label="Close-up photo of decorated pink and cream nail art with floral flourishes"></div>
</section>

</body>
</html>
```